Business Card Design - Law Firm

I need a business card design. I have attached a picture of the law firm's website and logo. The business card design should be consistent with those pictures. There should be a place for the employee name, employee job title, telephone number, facsimile number, address, website url, and email address for each employee.
Industry/Entity Type
Business

```html
<!DOCTYPE html>
<html lang="en">
<head>
<meta charset="utf-8">
<title>Halvorsen Law – Business Card</title>
<link rel="stylesheet" href="https://fonts.googleapis.com/css2?family=Ubuntu:wght@300;400&display=swap">
<style>
  :root {
    --card-bg: #000000;
    --text-white: #ffffff;
    --text-grey: #5c5c5c;
    --text-soft-grey: #8a8a8a;
    --accent-gold: #b59c5a;
    --accent-gold-bright: #d4b25a;
    --accent-red: #8e1b1b;
    --web-tone: #a39a88;
    --mark-fill: #1c1c1c;
  }
  * { margin: 0; padding: 0; box-sizing: border-box; }
  html, body {
    width: 1200px;
    height: 600px;
    overflow: hidden;
    background: var(--card-bg);
  }
  .card {
    position: relative;
    width: 1200px;
    height: 600px;
    background: var(--card-bg);
    font-family: "Ubuntu", sans-serif;
    color: var(--text-white);
    line-height: 1;
  }
  .card > * { position: absolute; white-space: nowrap; }

  .brand {
    left: 690px;
    top: 82px;
    display: flex;
    align-items: center;
    gap: 26px;
  }
  .brand-square {
    width: 56px;
    height: 56px;
    background: var(--mark-fill);
    border: 1px solid #3a3a3a;
  }
  .brand-name {
    font-weight: 300;
    font-size: 40px;
    letter-spacing: 4px;
    color: var(--accent-gold);
  }

  .employee-name {
    left: 56px;
    top: 326px;
    font-size: 48px;
    font-weight: 300;
    letter-spacing: 0.24em;
  }
  .employee-name .first { color: var(--text-white); }
  .employee-name .last { color: var(--text-grey); }

  .job-title {
    left: 351px;
    top: 384px;
    font-size: 17px;
    font-weight: 400;
  }

  .email {
    left: 56px;
    top: 430px;
    font-size: 17px;
    font-weight: 300;
    color: var(--text-soft-grey);
  }
  .email .domain { color: var(--accent-gold-bright); }

  .phone {
    left: 56px;
    top: 482px;
    font-size: 31px;
    font-weight: 300;
    letter-spacing: 0.2em;
  }
  .phone .code { color: var(--accent-red); }

  .address {
    left: 855px;
    top: 430px;
    font-size: 17px;
    line-height: 27px;
    font-weight: 400;
    font-style: normal;
  }

  .website {
    left: 855px;
    top: 498px;
    font-size: 17px;
    letter-spacing: 3px;
    color: var(--web-tone);
  }
</style>
</head>
<body>
  <main class="card">
    <div class="brand">
      <span class="brand-square"></span>
      <span class="brand-name">Halvorsen Law</span>
    </div>

    <h1 class="employee-name"><span class="first">Employer</span> <span class="last">Name</span></h1>
    <p class="job-title">Employer Job Title here</p>

    <p class="email">employermail<span class="domain">@example.com</span></p>
    <p class="phone"><span class="code">(+44)</span>0 123 123 123</p>

    <address class="address">48, Ferncliff road, Building 17,<br>Ashmoor, Westvale 4410.</address>
    <p class="website">www.halvorsen.com</p>
  </main>
</body>
</html>
```